Pharma business needs a catalogue design

Morvax Ltd. is a fast-growing pharma production company, and we need a catalogue design for white label products (as in unbranded ones). We would only want to distribute the catalogue digitally. Attached to this brief is our current product list.

We are also looking to upgrade the look of our product list so this is where you can display your creativity. Feel free to change up the look as much as you like in order to make it look better. You can also make it as long as you wish.

Important: Often times, our customers want to put their logo directly on our product catalogue. You should, therefore, design the catalogue with this in mind and make it simple for us to be able to replace the logo with another one.

The final design should communicate unwavering quality and incredible attention to detail.

Should you have any questions, please do not hesitate to contact us. We understand that any creative process takes joint effort and mutual understanding.

Industry/Entity Type

Pharmaceutical

Font styles to use
Decorative
Script

Colors

Designer to choose colors to be used in the design.

Requirements
Must have
• What is required is to change the photos of each product with tubes/boxes/packaging that just says "your brand here".

```html
<!DOCTYPE html>
<html lang="en">
<head>
<meta charset="utf-8">
<title>Morvax Ltd. – Product List 2019</title>
<link href="https://fonts.googleapis.com/css2?family=Barlow:wght@400;500;600;700&display=swap" rel="stylesheet">
<style>
:root{
  --bg:#4b4d57;
  --navy:#2a3f96;
  --navy-dark:#1f3283;
  --sky:#7cc3ec;
  --frame:#6fb5e6;
  --orange:#f3c08a;
  --green:#6cc42b;
  --paper:#ffffff;
  --paper-gray:#f1f2f4;
  --strip:#e6e7ea;
  --ink:#2c2e3a;
  --muted:#5a6ab0;
}
*{box-sizing:border-box;margin:0;padding:0}
html,body{width:1200px;height:1200px;overflow:hidden;background:var(--bg);font-family:'Barlow',sans-serif;color:var(--ink)}
.stage{position:absolute;left:0;top:0;width:1500px;height:1500px;transform:scale(.8);transform-origin:0 0}
.page{position:absolute;top:271px;width:686px;height:888px;background:var(--paper);overflow:hidden}
.page--vitamins{left:53px}
.page--extracts{left:764px}
.page--vitamins .content-bg{position:absolute;left:0;top:170px;width:100%;height:665px;background:var(--paper-gray)}

.header-band{position:absolute;left:150px;top:17px;right:0;height:60px;background:linear-gradient(90deg,var(--navy-dark) 0%,var(--navy) 40%,var(--sky) 100%)}
.header-title{position:absolute;left:150px;right:0;top:17px;height:60px;line-height:60px;text-align:center;color:#fff;font-size:33px;font-weight:500;letter-spacing:1px;padding-left:20px}
.header-strip{position:absolute;left:230px;right:0;top:77px;height:28px;background:linear-gradient(90deg,#fff 0%,var(--strip) 35%)}
.header-web{position:absolute;left:360px;width:260px;top:77px;line-height:28px;text-align:center;color:var(--navy);font-weight:700;font-size:15px}
.logo-oval{position:absolute;left:13px;top:10px;width:172px;height:80px;border:4px solid var(--navy);border-radius:50%;background:#fff;display:flex;align-items:center;justify-content:center;font-size:11px;font-weight:700;color:var(--navy)}

.section-banner{position:absolute;left:0;right:0;top:117px;height:52px;display:flex;align-items:center;padding-left:35px;color:#fff;font-size:23px;font-weight:700;letter-spacing:.3px;box-shadow:0 3px 3px rgba(0,0,0,.12)}
.section-banner--orange{background:var(--orange)}
.section-banner--green{background:var(--green)}
.section-icon{width:44px;height:40px;margin-right:18px;border-radius:50%;background:rgba(255,255,255,.35)}

.block{position:absolute}
.block-frame{position:absolute;border:3px solid var(--frame);background:transparent}
.block-bar{position:absolute;left:0;top:0;height:42px;background:var(--navy);border-radius:0 22px 22px 0;color:#fff;font-weight:600;font-size:13px;line-height:42px;padding-left:35px;z-index:2}
.block-bar::after{content:"";position:absolute;left:0;top:42px;border-top:10px solid var(--navy-dark);border-right:10px solid transparent}
.block-pill{position:absolute;top:0;height:42px;background:var(--sky);border-radius:0 22px 22px 0;color:#fff;font-weight:600;font-size:12.5px;line-height:15px;padding:5px 0 0 70px;z-index:1}
.pack{position:absolute;width:148px;background:#fff;box-shadow:0 2px 5px rgba(0,0,0,.18);z-index:2}
.pack-art{position:absolute;background:linear-gradient(180deg,#f4f5f7,#dfe2e7);display:flex;align-items:center;justify-content:center;text-align:center;color:#8b95b8;font-size:7px;line-height:8px;font-weight:600}
.pack-logo{position:absolute;right:14px;top:12px;width:72px;height:28px;border:1px dashed var(--frame);font-size:11px;color:var(--muted);display:flex;align-items:center;justify-content:center}
.pack-caption{position:absolute;left:0;right:0;bottom:10px;text-align:center;font-size:10.5px;color:var(--muted)}
.facts{position:absolute;display:flex;gap:35px;z-index:2}
.facts-col{width:170px}
.fact{display:flex;font-size:11.8px;line-height:14.8px;white-space:nowrap}
.fact .lead{flex:1;border-bottom:1px dotted #555;margin:0 1px 4px}

.footer-rule{position:absolute;left:0;right:0;height:4px}
.footer{position:absolute;left:0;right:0;height:40px;font-size:11px;color:var(--muted);display:flex;align-items:center}
.footer-item{position:absolute;display:flex;align-items:center;gap:10px;line-height:13px}
.footer-item svg{width:16px;height:16px}
</style>
</head>
<body>
<div class="stage">

  <!-- Page 1: vitamins & minerals -->
  <section class="page page--vitamins">
    <div class="content-bg"></div>
    <div class="header-band"></div>
    <div class="header-title">PRODUCT LIST 2019</div>
    <div class="header-strip"></div>
    <div class="header-web">www.website.com</div>
    <div class="logo-oval">LOGO</div>
    <div class="section-banner section-banner--orange"><span class="section-icon" role="img" aria-label="Citrus fruit icon"></span>VITAMINS &amp; MINERALS - EFFERVESCENT PRODUCTS</div>

    <div class="block" style="left:20px;top:183px;width:640px;height:256px">
      <div class="block-frame" style="left:15px;top:17px;width:625px;height:238px"></div>
      <div class="block-pill" style="left:300px;width:225px">4000 mg/tablet<br>(Citrus flavor)</div>
      <div class="block-bar" style="width:372px">A-Z +Lutein and Selenium</div>
      <div class="pack" style="left:30px;top:57px;height:178px">
        <div class="pack-art" role="img" aria-label="Effervescent tube reading Your brand here" style="left:48px;top:55px;width:30px;height:92px">YOUR BRAND HERE</div>
        <div class="pack-logo">LOGO</div>
        <div class="pack-caption">20 Tablets in tube</div>
      </div>
      <div class="facts" style="left:240px;top:60px">
        <div class="facts-col">
          <div class="fact">Calcium<span class="lead"></span>160 mg</div>
          <div class="fact">Magnesium<span class="lead"></span>60 mg</div>
          <div class="fact">Vitamin C<span class="lead"></span>60 mg</div>
          <div class="fact">Vitamin B3<span class="lead"></span>18 mg</div>
          <div class="fact">Ferrum<span class="lead"></span>10 mg</div>
          <div class="fact">Vitamin E<span class="lead"></span>10 mg</div>
          <div class="fact">Pantothenic acid<span class="lead"></span>6 mg</div>
          <div class="fact">Zinc<span class="lead"></span>5 mg</div>
          <div class="fact">Vitamin B2<span class="lead"></span>2,97 mg</div>
          <div class="fact">Vitamin B6<span class="lead"></span>2 mg</div>
          <div class="fact">Vitamin B1<span class="lead"></span>1,4 mg</div>
          <div class="fact">Vitamin A<span class="lead"></span>800 µg</div>
        </div>
        <div class="facts-col">
          <div class="fact">Copper<span class="lead"></span>0,5 mg</div>
          <div class="fact">Manganese<span class="lead"></span>0,4 mg</div>
          <div class="fact">Folat<span class="lead"></span>200 µg</div>
          <div class="fact">Vitamin H<span class="lead"></span>150 µg</div>
          <div class="fact">Iodine<span class="lead"></span>100 µg</div>
          <div class="fact">Lutein<span class="lead"></span>50 µg</div>
          <div class="fact">Vitamin K1<span class="lead"></span>30 µg</div>
          <div class="fact">Selenium<span class="lead"></span>30 µg</div>
          <div class="fact">Cromium<span class="lead"></span>25 µg</div>
          <div class="fact">Molybdenum<span class="lead"></span>25 µg</div>
          <div class="fact">Vitamin D3<span class="lead"></span>5 µg</div>
          <div class="fact">Vitamin B12<span class="lead"></span>1 µg</div>
        </div>
      </div>
    </div>

    <div class="block" style="left:25px;top:451px;width:640px;height:182px">
      <div class="block-frame" style="left:15px;top:16px;width:626px;height:165px"></div>
      <div class="block-pill" style="left:300px;width:225px">4000 mg/tablet<br>(Orange flavor)</div>
      <div class="block-bar" style="width:372px">MULTIVITAMINS +Biotin</div>
      <div class="pack" style="left:32px;top:55px;height:110px">
        <div class="pack-art" role="img" aria-label="Effervescent tube reading Your brand here" style="left:40px;top:15px;width:24px;height:70px">YOUR BRAND HERE</div>
        <div class="pack-logo">LOGO</div>
        <div class="pack-caption">20 Tablets in tube</div>
      </div>
      <div class="facts" style="left:231px;top:60px">
        <div class="facts-col">
          <div class="fact">Vitamin A<span class="lead"></span>900 µg</div>
          <div class="fact">Vitamin E<span class="lead"></span>6,90 mg</div>
          <div class="fact">Vitamin B1<span class="lead"></span>1,80 mg</div>
          <div class="fact">Vitamin B2<span class="lead"></span>1,45 mg</div>
          <div class="fact">Vitamin B6<span class="lead"></span>1,70 mg</div>
          <div class="fact">Vitamin B12<span class="lead"></span>5 µg</div>
          <div class="fact">Vitamin C<span class="lead"></span>75 mg</div>
        </div>
        <div class="facts-col">
          <div class="fact">Folic acid<span class="lead"></span>200 µg</div>
          <div class="fact">Nicotinamide<span class="lead"></span>20 mg</div>
          <div class="fact">Vitamin D3<span class="lead"></span>5 µg</div>
          <div class="fact">Vitamin B5<span class="lead"></span>10 mg</div>
          <div class="fact">Beta Carotene<span class="lead"></span>0,50 mg</div>
          <div class="fact">Biotin<span class="lead"></span>50 µg</div>
        </div>
      </div>
    </div>

    <div class="block" style="left:25px;top:642px;width:640px;height:182px">
      <div class="block-frame" style="left:15px;top:16px;width:626px;height:164px"></div>
      <div class="block-pill" style="left:300px;width:225px">4000 mg/tablet<br>(Orange flavor)</div>
      <div class="block-bar" style="width:372px">ACTIVE + Q10</div>
      <div class="pack" style="left:32px;top:55px;height:108px">
        <div class="pack-art" role="img" aria-label="Effervescent tube reading Your brand here" style="left:40px;top:12px;width:24px;height:70px">YOUR BRAND HERE</div>
        <div class="pack-logo">LOGO</div>
        <div class="pack-caption">20 Tablets in tube</div>
      </div>
      <div class="facts" style="left:232px;top:50px">
        <div class="facts-col">
          <div class="fact">Vitamin E<span class="lead"></span>16,50 mg</div>
          <div class="fact">Vitamin B1<span class="lead"></span>2,60 mg</div>
          <div class="fact">Vitamin B2<span class="lead"></span>1,90 mg</div>
          <div class="fact">Vitamin B6<span class="lead"></span>4,00 mg</div>
          <div class="fact">Vitamin B12<span class="lead"></span>4,95 µg</div>
          <div class="fact">Vitamin C<span class="lead"></span>160 mg</div>
          <div class="fact">Folic acid<span class="lead"></span>200 µg</div>
          <div class="fact">Nicotinamide<span class="lead"></span>19,80 mg</div>
        </div>
        <div class="facts-col">
          <div class="fact">Vitamin D3<span class="lead"></span>5 µg</div>
          <div class="fact">Copper<span class="lead"></span>0,45 mg</div>
          <div class="fact">Iron<span class="lead"></span>2,70 mg</div>
          <div class="fact">Magnesium<span class="lead"></span>60 mg</div>
          <div class="fact">Zinc<span class="lead"></span>2,70 mg</div>
          <div class="fact">Manganese<span class="lead"></span>0,90 mg</div>
          <div class="fact">Beta Carotene<span class="lead"></span>0,5 mg</div>
          <div class="fact">Coenzyme Q10<span class="lead"></span>2,00 mg</div>
        </div>
      </div>
    </div>

    <div class="footer-rule" style="top:834px;background:var(--orange)"></div>
    <div class="footer" style="top:843px">
      <div class="footer-item" style="left:36px"><svg viewBox="0 0 16 16"><path d="M8 1a5 5 0 0 0-5 5c0 4 5 9 5 9s5-5 5-9a5 5 0 0 0-5-5z" fill="none" stroke="#4a64c0" stroke-width="1.6"/><circle cx="8" cy="6" r="1.8" fill="#4a64c0"/></svg><span>Address 1<br>Address 2</span></div>
      <div class="footer-item" style="left:270px"><svg viewBox="0 0 16 16"><path d="M3 2l3 0 1 3-2 1.5a8 8 0 0 0 4.5 4.5L11 9l3 1v3c-6 1-12-5-11-11z" fill="none" stroke="#4a64c0" stroke-width="1.5"/></svg><span>Phone Number</span></div>
      <div class="footer-item" style="left:524px"><svg viewBox="0 0 16 16"><rect x="1" y="3" width="14" height="10" fill="none" stroke="#4a64c0" stroke-width="1.5"/><path d="M1 3l7 6 7-6" fill="none" stroke="#4a64c0" stroke-width="1.5"/></svg><span>office@email.com</span></div>
    </div>
  </section>

  <!-- Page 2: natural extracts -->
  <section class="page page--extracts">
    <div class="header-band"></div>
    <div class="header-title">PRODUCT LIST 2019</div>
    <div class="header-strip"></div>
    <div class="header-web">www.website.com</div>
    <div class="logo-oval">LOGO</div>
    <div class="section-banner section-banner--green"><span class="section-icon" role="img" aria-label="Leaf icon"></span>PRODUCTS WITH NATURAL EXTRACTS</div>

    <div class="block" style="left:20px;top:193px;width:645px;height:192px">
      <div class="block-frame" style="left:12px;top:17px;width:630px;height:175px"></div>
      <div class="block-bar" style="width:372px">GINKGO BILIBA + Mg</div>
      <div class="pack" style="left:30px;top:52px;height:122px">
        <div class="pack-art" role="img" aria-label="Capsule box reading Your brand here" style="left:16px;top:30px;width:72px;height:62px">YOUR<br>BRAND<br>HERE</div>
        <div class="pack-logo" style="right:6px;top:6px">LOGO</div>
        <div class="pack-caption">2 blisters x 15 capsules in box</div>
      </div>
      <div class="facts" style="left:235px;top:58px">
        <div class="facts-col">
          <div class="fact">Ginkgo Biloba extract<span class="lead"></span>40 mg</div>
          <div class="fact">Magnesium<span class="lead"></span>60 mg</div>
        </div>
      </div>
    </div>

    <div class="block" style="left:22px;top:406px;width:645px;height:192px">
      <div class="block-frame" style="left:12px;top:16px;width:630px;height:175px"></div>
      <div class="block-bar" style="width:372px">GINKGO BILOBA FORTE</div>
      <div class="pack" style="left:30px;top:52px;height:130px">
        <div class="pack-art" role="img" aria-label="Capsule box reading Your brand here" style="left:20px;top:38px;width:72px;height:62px">YOUR<br>BRAND<br>HERE</div>
        <div class="pack-logo" style="right:6px;top:6px">LOGO</div>
        <div class="pack-caption">4 blisters x 15 capsules in box</div>
      </div>
      <div class="facts" style="left:235px;top:60px">
        <div class="facts-col">
          <div class="fact">Ginkgo Biloba extract-120 mg</div>
          <div class="fact">Green tea extract<span class="lead"></span>30 mg</div>
          <div class="fact">Vitamin B6<span class="lead"></span>1,4 mg</div>
          <div class="fact">Magnesium<span class="lead"></span>150 mg</div>
          <div class="fact">Selenium<span class="lead"></span>55 µg</div>
        </div>
      </div>
    </div>

    <div class="block" style="left:24px;top:618px;width:645px;height:192px">
      <div class="block-frame" style="left:12px;top:16px;width:630px;height:175px"></div>
      <div class="block-bar" style="width:372px">GINSENG + Propolis &amp; Vitamin E</div>
      <div class="pack" style="left:30px;top:52px;height:130px">
        <div class="pack-art" role="img" aria-label="Capsule box reading Your brand here" style="left:18px;top:38px;width:72px;height:62px">YOUR<br>BRAND<br>HERE</div>
        <div class="pack-logo" style="right:6px;top:6px">LOGO</div>
        <div class="pack-caption">2 blisters x 15 capsules in box</div>
      </div>
      <div class="facts" style="left:233px;top:60px">
        <div class="facts-col">
          <div class="fact">Ginseng extract<span class="lead"></span>100 mg</div>
          <div class="fact">Propolis<span class="lead"></span>250 mg</div>
          <div class="fact">Vitamin E<span class="lead"></span>10 mg</div>
        </div>
      </div>
    </div>

    <div class="footer-rule" style="top:837px;background:var(--green)"></div>
    <div class="footer" style="top:846px">
      <div class="footer-item" style="left:36px"><svg viewBox="0 0 16 16"><path d="M8 1a5 5 0 0 0-5 5c0 4 5 9 5 9s5-5 5-9a5 5 0 0 0-5-5z" fill="none" stroke="#4a64c0" stroke-width="1.6"/><circle cx="8" cy="6" r="1.8" fill="#4a64c0"/></svg><span>Address 1<br>Address 2</span></div>
      <div class="footer-item" style="left:270px"><svg viewBox="0 0 16 16"><path d="M3 2l3 0 1 3-2 1.5a8 8 0 0 0 4.5 4.5L11 9l3 1v3c-6 1-12-5-11-11z" fill="none" stroke="#4a64c0" stroke-width="1.5"/></svg><span>Phone Number</span></div>
      <div class="footer-item" style="left:524px"><svg viewBox="0 0 16 16"><rect x="1" y="3" width="14" height="10" fill="none" stroke="#4a64c0" stroke-width="1.5"/><path d="M1 3l7 6 7-6" fill="none" stroke="#4a64c0" stroke-width="1.5"/></svg><span>office@email.com</span></div>
    </div>
  </section>

</div>
</body>
</html>
```